Business Card Design Project

I have attached the logo and the colour pallete for the branding for the company.

Creative designs for business cards are needed.

The Company is modern corporate.

Industry/Entity Type

Business

```html
<!DOCTYPE html>
<html lang="en">
<head>
<meta charset="utf-8">
<title>Trailmark Business Cards</title>
<link rel="stylesheet" href="https://fonts.googleapis.com/css2?family=Open+Sans:wght@400;600;700;800&display=swap">
<style>
  :root {
    --canvas-bg: #e9e7e3;
    --card-white: #ffffff;
    --ink: #111111;
    --ink-soft: #3a3a3a;
    --black-panel: #0d0d0d;
    --back-center: #2c2c2c;
    --back-edge: #050505;
    --accent-orange: #f08a24;
    --accent-red: #e2203c;
    --muted-line: #9a9a9a;
  }
  * { margin: 0; padding: 0; box-sizing: border-box; }
  html, body {
    width: 1200px; height: 1024px; overflow: hidden;
    background: var(--canvas-bg);
    font-family: "Open Sans", Arial, sans-serif;
  }
  .sheet {
    width: 1200px; height: 1024px;
    display: flex; flex-direction: column; align-items: center; justify-content: center;
    gap: 60px;
  }
  .card {
    position: relative;
    width: 700px; height: 400px;
    overflow: hidden;
    box-shadow: 0 10px 28px rgba(0,0,0,0.22);
  }
  /* Front */
  .card-front { background: var(--card-white); }
  .card-front .art { position: absolute; inset: 0; }
  .brand-name {
    position: absolute;
    font-weight: 800;
    letter-spacing: -1px;
    line-height: 1;
  }
  .card-front .brand-name {
    left: 60px; top: 120px;
    font-size: 64px; color: var(--ink);
  }
  .holder {
    position: absolute; left: 60px; top: 244px;
  }
  .holder-name { font-size: 22px; font-weight: 800; color: var(--ink); line-height: 1.1; }
  .holder-title { font-size: 14px; font-weight: 600; color: var(--accent-orange); margin-bottom: 6px; }
  .holder-address { font-size: 15px; color: var(--ink-soft); line-height: 1.35; }
  .contact-list {
    position: absolute; right: 40px; top: 38px;
    list-style: none;
    font-size: 15px; color: var(--ink-soft); line-height: 1.75;
  }
  .contact-list li { display: flex; align-items: center; gap: 8px; }
  .contact-list svg { width: 13px; height: 13px; flex: none; }
  .front-web {
    position: absolute; right: 40px; bottom: 34px;
    font-size: 15px; color: #ffffff; letter-spacing: 0.3px;
  }
  /* Back */
  .card-back {
    background: radial-gradient(ellipse at 50% 45%, var(--back-center) 0%, var(--back-edge) 75%);
  }
  .card-back .brand-name {
    left: 0; right: 0; top: 150px; text-align: center;
    font-size: 92px; color: #ffffff;
  }
  .back-web {
    position: absolute; left: 60px; bottom: 38px;
    font-size: 15px; color: #d6d6d6; letter-spacing: 0.3px;
  }
</style>
</head>
<body>
<main class="sheet">
  <section class="card card-front" aria-label="Business card front">
    <svg class="art" viewBox="0 0 700 400" aria-hidden="true">
      <defs>
        <linearGradient id="swoosh" x1="0" y1="1" x2="1" y2="0">
          <stop offset="0" stop-color="var(--accent-red)"/>
          <stop offset="1" stop-color="var(--accent-orange)"/>
        </linearGradient>
        <linearGradient id="rule" x1="0" x2="1">
          <stop offset="0" stop-color="#ffffff"/>
          <stop offset="0.5" stop-color="var(--muted-line)"/>
          <stop offset="1" stop-color="#ffffff"/>
        </linearGradient>
      </defs>
      <path d="M700 150 C560 190 420 300 330 400 L700 400 Z" fill="var(--black-panel)"/>
      <path d="M0 398 C260 396 490 340 640 182" fill="none" stroke="url(#swoosh)" stroke-width="7"/>
      <path d="M622 170 L668 160 L650 202 Z" fill="var(--accent-orange)"/>
      <rect x="420" y="150" width="150" height="2" fill="url(#rule)"/>
    </svg>
    <div class="brand-name">Trailmark</div>
    <div class="holder">
      <div class="holder-name">YOUR NAME</div>
      <div class="holder-title">Job Title</div>
      <div class="holder-address">Your address goes here,<br>City, Zip code, State, Country name</div>
    </div>
    <ul class="contact-list">
      <li><svg viewBox="0 0 12 12"><rect x="2" y="0.5" width="8" height="11" rx="1.5" fill="none" stroke="var(--accent-red)" stroke-width="1.3"/></svg>000-000-000</li>
      <li><svg viewBox="0 0 12 12"><path d="M2.5 1 L5 1 L5.8 3.5 L4.3 4.6 C5 6 6 7 7.4 7.7 L8.5 6.2 L11 7 L11 9.5 C6 10 2 6 2.5 1 Z" fill="var(--accent-red)"/></svg>000-0000-000</li>
      <li><svg viewBox="0 0 12 12"><rect x="0.5" y="2" width="11" height="8" fill="var(--accent-red)"/><path d="M0.5 2 L6 6.5 L11.5 2" fill="none" stroke="#fff" stroke-width="1"/></svg>name@domainname.com</li>
    </ul>
    <div class="front-web">www.domainname.com</div>
  </section>

  <section class="card card-back" aria-label="Business card back">
    <div class="brand-name">Trailmark</div>
    <div class="back-web">www.domainname.com</div>
  </section>
</main>
</body>
</html>
```